new Business card Design

I need a new Business Card with my logo and ned a modern, elegant and expensive looking business card.
i Upload my Logo and the actual business card for example

```html
<!DOCTYPE html>
<html lang="de">
<head>
<meta charset="utf-8">
<title>Velora Motors – Visitenkarte</title>
<link href="https://fonts.googleapis.com/css2?family=Raleway:wght@400;500;600;700&display=swap" rel="stylesheet">
<style>
  :root {
    --bg: #2b2d31;
    --card: #ffffff;
    --ink: #2e3034;
    --muted: #6b6e73;
    --red: #e3191f;
    --grey-light: #77797d;
    --grey-dark: #4a4c50;
  }
  * { margin: 0; padding: 0; box-sizing: border-box; }
  html, body {
    width: 1200px; height: 900px; overflow: hidden;
    background: var(--bg);
    font-family: "Raleway", sans-serif;
    color: var(--ink);
  }
  .stage { position: relative; width: 1200px; height: 900px; }
  .card {
    position: absolute; left: 300px;
    width: 600px; height: 388px;
    background: var(--card);
    border-radius: 18px;
    overflow: hidden;
    box-shadow: 0 14px 30px rgba(0,0,0,.45);
  }
  .card--contact { top: 46px; }
  .card--brand { top: 466px; }
  .card .decor { position: absolute; inset: 0; width: 100%; height: 100%; }

  .brand { display: flex; flex-direction: column; }
  .brand__row { display: flex; align-items: center; gap: 12px; }
  .brand__dot { width: 28px; height: 28px; border-radius: 50%; background: var(--red); flex: none; }
  .brand__name { font-weight: 700; font-size: 36px; color: var(--ink); letter-spacing: -.3px; line-height: 1; }
  .brand__tagline { font-size: 12px; font-weight: 500; color: var(--muted); margin: 6px 0 0 40px; letter-spacing: .3px; }

  .card--contact .brand { position: absolute; left: 36px; top: 36px; }
  .card--contact .brand__name { font-size: 32px; }
  .card--contact .brand__dot { width: 24px; height: 24px; }
  .card--contact .brand__tagline { font-size: 11px; margin-left: 36px; }

  .person { position: absolute; left: 40px; top: 132px; }
  .person__name { font-size: 22px; font-weight: 600; letter-spacing: .6px; color: var(--ink); }
  .person__name span { color: var(--red); }
  .person__role { font-size: 11px; letter-spacing: 1.4px; color: var(--muted); margin-top: 4px; }

  .contacts { position: absolute; left: 40px; top: 200px; list-style: none; }
  .contacts li { display: flex; align-items: center; gap: 12px; font-size: 14px; font-weight: 500; color: var(--ink); height: 27px; }
  .contacts svg { width: 15px; height: 15px; flex: none; fill: var(--red); }
  .contacts .lines { display: flex; flex-direction: column; line-height: 1.25; }
  .contacts li.phone { height: 44px; }

  .card--brand .brand { position: absolute; left: 0; right: 0; top: 128px; align-items: center; }
</style>
</head>
<body>
<main class="stage">

  <section class="card card--contact">
    <svg class="decor" viewBox="0 0 600 388" role="img" aria-label="Dekorfläche in Rot und Grau">
      <defs>
        <radialGradient id="fade-a" cx="690" cy="440" r="310" gradientUnits="userSpaceOnUse">
          <stop offset="0.5" stop-color="var(--grey-dark)"/>
          <stop offset="0.9" stop-color="var(--grey-light)"/>
          <stop offset="1" stop-color="var(--red)"/>
        </radialGradient>
      </defs>
      <circle cx="690" cy="440" r="310" fill="url(#fade-a)"/>
    </svg>

    <div class="brand">
      <div class="brand__row"><span class="brand__dot"></span><span class="brand__name">Velora Motors</span></div>
      <div class="brand__tagline">Handel | Service | Werkstatt</div>
    </div>

    <div class="person">
      <div class="person__name">DARIO <span>KELLENBERG</span></div>
      <div class="person__role">GESCHÄFTSFÜHRER</div>
    </div>

    <ul class="contacts">
      <li class="phone">
        <svg viewBox="0 0 24 24"><path d="M6.6 10.8a15.1 15.1 0 0 0 6.6 6.6l2.2-2.2a1 1 0 0 1 1-.25 11.4 11.4 0 0 0 3.6.57 1 1 0 0 1 1 1V20a1 1 0 0 1-1 1A17 17 0 0 1 3 4a1 1 0 0 1 1-1h3.5a1 1 0 0 1 1 1c0 1.25.2 2.45.57 3.57a1 1 0 0 1-.25 1z"/></svg>
        <span class="lines"><span>062 555 01 23</span><span>078 555 02 46</span></span>
      </li>
      <li>
        <svg viewBox="0 0 24 24"><path d="M2 5h20v14H2z M4 7v.4l8 5.2 8-5.2V7z" fill-rule="evenodd"/></svg>
        <span>info@veloramotors.ch</span>
      </li>
      <li>
        <svg viewBox="0 0 24 24"><path d="M12 2a10 10 0 1 0 0 20 10 10 0 0 0 0-20zm6.9 9h-3a15 15 0 0 0-1.3-6 8 8 0 0 1 4.3 6zM12 4.1c.9 1.3 1.7 3.7 1.9 6.9h-3.8c.2-3.2 1-5.6 1.9-6.9zM9.4 5a15 15 0 0 0-1.3 6h-3a8 8 0 0 1 4.3-6zM5.1 13h3a15 15 0 0 0 1.3 6 8 8 0 0 1-4.3-6zm6.9 6.9c-.9-1.3-1.7-3.7-1.9-6.9h3.8c-.2 3.2-1 5.6-1.9 6.9zm2.6-.9a15 15 0 0 0 1.3-6h3a8 8 0 0 1-4.3 6z"/></svg>
        <span>www.veloramotors.ch</span>
      </li>
      <li>
        <svg viewBox="0 0 24 24"><path d="M12 2a7 7 0 0 0-7 7c0 5.2 7 13 7 13s7-7.8 7-13a7 7 0 0 0-7-7zm0 9.5A2.5 2.5 0 1 1 12 6.5a2.5 2.5 0 0 1 0 5z"/></svg>
        <span>Lindenweg 7 4600 Musterdorf</span>
      </li>
    </ul>
  </section>

  <section class="card card--brand">
    <svg class="decor" viewBox="0 0 600 388" role="img" aria-label="Dekorflächen in Rot und Grau">
      <defs>
        <radialGradient id="fade-b" cx="620" cy="-30" r="140" gradientUnits="userSpaceOnUse">
          <stop offset="0.5" stop-color="var(--grey-dark)"/>
          <stop offset="0.88" stop-color="var(--grey-light)"/>
          <stop offset="1" stop-color="var(--red)"/>
        </radialGradient>
        <radialGradient id="fade-c" cx="240" cy="500" r="230" gradientUnits="userSpaceOnUse">
          <stop offset="0.5" stop-color="var(--grey-dark)"/>
          <stop offset="0.9" stop-color="var(--grey-light)"/>
          <stop offset="1" stop-color="var(--red)"/>
        </radialGradient>
      </defs>
      <circle cx="620" cy="-30" r="140" fill="url(#fade-b)"/>
      <circle cx="240" cy="500" r="230" fill="url(#fade-c)"/>
    </svg>

    <div class="brand">
      <div class="brand__row"><span class="brand__dot"></span><span class="brand__name">Velora Motors</span></div>
      <div class="brand__tagline">Handel | Service | Werkstatt</div>
    </div>
  </section>

</main>
</body>
</html>
```